A poster for Vale Chiropractic's up coming powerful health workshop/seminar

I need a poster developed for Dr. Prent's upcoming Total Shape Reset and Armor Plating your Wellness seminar/workshop. This workshop will teach attendants how to shed pounds and rapidly reduce their waist size. Learn why weight loss doesn't work 99.9% of the time so that you can be the successful .1%. It's time to expose the LIES and reveal the TRUTH about the REAL causes of HEART DISEASE, DIABETES, CANCER, CHRONIC FATIGUE, ARTHRITIS, FIBROMYALGIA, and how to REVERSE/PREVENT this from ever happening to you or your family. The Insider Secrets to building your body into a health fortress unbreachable by sickness and disease. Learn to live and fufill your GOD-GIVEN health potential. Eliminate high bloodpressure, high cholesterol, diabetes, fatigue, chronic pain
Ending the WAR on sickness and disease by launching an unstoppable health offensive that will pummel any enemy of life and health.

I'm not a designer by any means, but was thinking of possible WAR theme, cammo, etc....just a thought. Not a requirement by any means
Updates

Dr. Prent has taken a look at all the submissions and has requested a few changes.

1. He wants the new map that has been added to the brief with Marlow Ridge College as a title above the map

2. He wants a section that describes what the attendees will gain at the seminar in bullet format.  Example:  Title....It's not about what you lose

                                                   I'ts about what you gain....

>The No-Hype, No- Gimmick  secrets for fast effective Weight loss

>How the top 3 disease killers, heart disease, cancer, and diabetes are linked to diet

>Tools and strategies to make 2012 the best year ever

The Seminar will be held at Marlow Ridge College, Tuesday January 3rd @ 6:30pm Open to Public

Target Market(s)

Adults 30-65

Industry/Entity Type

Building

Requirements
Should not have
• ruyrtur

```html
<!DOCTYPE html>
<html lang="en">
<head>
<meta charset="utf-8">
<title>Total Shape Reset and Armor Plating your Wellness Seminar</title>
<link href="https://fonts.googleapis.com/css2?family=Rokkitt:wght@500&family=Francois+One&family=Tinos:wght@400;700&family=PT+Sans:wght@400;700&family=Courgette&display=swap" rel="stylesheet">
<style>
  :root {
    --page: #ffffff;
    --sun-yellow: #fdd03a;
    --sun-light: #fde27a;
    --sun-deep: #f9b912;
    --accent-orange: #f26b21;
    --band-orange: #f26a24;
    --title-yellow: #ffe81a;
    --leaf-green: #6cb52f;
    --leaf-dark: #2f7d2b;
    --sky-panel: #9ad4e3;
    --teal-text: #1b6f8e;
    --heading-teal: #1c7893;
    --badge-blue: #1f5aa6;
    --steel: #b9bcc0;
    --steel-dark: #6f7378;
    --portrait-dark: #3a2a22;
    --portrait-warm: #7a5a44;
    --map-land: #e4e8d6;
    --map-road: #c9cdb8;
  }
  * { margin: 0; padding: 0; box-sizing: border-box; }
  html, body { width: 927px; height: 1200px; overflow: hidden; background: var(--page); }
  .poster { position: relative; width: 927px; height: 1200px; overflow: hidden; background: var(--page); }

  .hero {
    position: absolute; left: 20px; top: 14px; width: 889px; height: 514px;
    border-radius: 26px;
    background: radial-gradient(circle at 52% 40%, var(--sun-light) 0%, var(--sun-yellow) 45%, var(--sun-deep) 100%);
  }
  .notch { position: absolute; width: 0; height: 0; }
  .notch--hero-left { left: 20px; top: 360px; border-top: 14px solid transparent; border-bottom: 14px solid transparent; border-left: 14px solid var(--page); }
  .notch--hero-bottom { left: 700px; top: 514px; border-left: 14px solid transparent; border-right: 14px solid transparent; border-bottom: 14px solid var(--page); }

  .helmet {
    position: absolute; left: 336px; top: 50px; width: 250px; height: 380px;
    border-radius: 46% 46% 30% 30%;
    background: linear-gradient(135deg, #e8eaec 0%, var(--steel) 45%, var(--steel-dark) 100%);
  }
  .quote-mark {
    position: absolute; color: #fff; font-family: "Tinos", serif; font-weight: 700;
    font-size: 150px; line-height: 1;
  }
  .quote-mark--open { left: 238px; top: 80px; }
  .quote-mark--close { left: 660px; top: 104px; }

  .tagline {
    position: absolute; color: var(--accent-orange);
    font-family: "Rokkitt", serif; font-weight: 500; font-size: 30px; line-height: 1.2;
  }
  .tagline--left { left: 40px; top: 244px; }
  .tagline--right { left: 610px; top: 214px; width: 290px; text-align: center; line-height: 1.25; }

  .title-band {
    position: absolute; left: 0; top: 530px; width: 927px; height: 150px;
    background: var(--band-orange);
  }
  .title-badge { position: absolute; left: 57px; top: 502px; width: 158px; height: 120px; }
  .title-text {
    position: absolute; left: 224px; top: 534px;
    font-family: "Francois One", sans-serif; font-weight: 400; font-size: 38px; line-height: 1.18;
    color: var(--title-yellow);
  }
  .event-details {
    position: absolute; left: 43px; top: 640px;
    font-family: "Tinos", serif; font-weight: 700; font-size: 23px; color: #fff;
    white-space: nowrap;
  }

  .info-panel {
    position: absolute; left: 20px; top: 690px; width: 889px; height: 530px;
    border-radius: 26px; background: var(--sky-panel);
  }
  .notch--info-right { left: 895px; top: 990px; border-top: 14px solid transparent; border-bottom: 14px solid transparent; border-right: 14px solid var(--page); }
  .notch--info-bottom { left: 280px; top: 1186px; border-left: 14px solid transparent; border-right: 14px solid transparent; border-bottom: 14px solid var(--page); }

  .welcome {
    position: absolute; left: 43px; top: 708px;
    font-family: "Tinos", serif; font-weight: 400; font-size: 28px; color: var(--heading-teal);
    text-decoration: underline; text-underline-offset: 6px; text-decoration-thickness: 1px;
  }
  .benefits { list-style: none; position: absolute; left: 10px; top: 776px; width: 560px; }
  .benefit {
    position: absolute; left: 0; display: flex; gap: 8px;
    font-family: "PT Sans", sans-serif; font-size: 16px; line-height: 1.2; color: var(--teal-text);
  }
  .benefit__icon { flex: 0 0 36px; height: 32px; margin-top: 2px; }
  .benefit__text { width: 500px; }

  .gains { position: absolute; left: 43px; top: 1100px; width: 530px; color: var(--teal-text); font-family: "PT Sans", sans-serif; }
  .gains__title { font-size: 15px; font-weight: 700; line-height: 1.2; color: var(--heading-teal); }
  .gains__list { list-style: none; font-size: 14px; line-height: 1.25; margin-top: 2px; }
  .gains__list li::before { content: "\203A\00a0"; font-weight: 700; color: var(--badge-blue); }

  .portrait-frame {
    position: absolute; left: 593px; top: 753px; width: 286px; height: 300px;
    background: #fff; padding: 7px;
  }
  .portrait {
    width: 100%; height: 100%;
    background: radial-gradient(circle at 50% 40%, var(--portrait-warm) 0%, var(--portrait-dark) 75%);
  }
  .speaker-name {
    position: absolute; left: 593px; top: 1050px; width: 286px; text-align: center;
    font-family: "Courgette", cursive; font-size: 36px; color: var(--badge-blue);
  }

  .venue { position: absolute; left: 593px; top: 1102px; width: 286px; }
  .venue__title {
    font-family: "PT Sans", sans-serif; font-weight: 700; font-size: 15px; line-height: 1.2;
    color: var(--heading-teal); text-align: center;
  }
  .venue__map {
    margin-top: 3px; height: 62px; border: 3px solid #fff;
    background: linear-gradient(135deg, var(--map-land) 0%, var(--map-road) 100%);
  }
</style>
</head>
<body>
<main class="poster">
  <section class="hero"></section>
  <span class="notch notch--hero-left"></span>
  <span class="notch notch--hero-bottom"></span>
  <div class="helmet" role="img" aria-label="Polished steel knight's helmet with brass rivets, symbolising protected health"></div>
  <span class="quote-mark quote-mark--open">&ldquo;</span>
  <span class="quote-mark quote-mark--close">&rdquo;</span>
  <p class="tagline tagline--left">Ending the War on<br>Sickness &amp; Diseases!</p>
  <p class="tagline tagline--right">Building your body<br>healthy-Protected<br>from all diseases!</p>

  <section class="title-band"></section>
  <svg class="title-badge" viewBox="0 0 158 120" aria-hidden="true">
    <rect x="0" y="0" width="150" height="14" rx="3" fill="var(--leaf-dark)"/>
    <rect x="0" y="8" width="158" height="112" fill="var(--leaf-green)"/>
    <path d="M48 36 L66 64 L48 92 L60 92 L78 64 L60 36 Z" fill="#fff"/>
    <path d="M78 36 L96 64 L78 92 L90 92 L108 64 L90 36 Z" fill="#fff"/>
  </svg>
  <h1 class="title-text">Total Shape Reset and Armor<br>Plating your Wellness Seminar/Workshop</h1>
  <p class="event-details">(Tuesday January 3rd @ 6:30pm &middot; Open to Public&nbsp;&nbsp;&nbsp;&nbsp;Venue : Marlow Ridge College)</p>

  <section class="info-panel"></section>
  <span class="notch notch--info-right"></span>
  <span class="notch notch--info-bottom"></span>
  <h2 class="welcome">Welcome to Our Health Seminar!</h2>

  <ul class="benefits">
    <li class="benefit" style="top:0">
      <svg class="benefit__icon" viewBox="0 0 36 32" aria-hidden="true"><rect width="36" height="32" rx="3" fill="var(--badge-blue)"/><path d="M9 8 L16 16 L9 24 L13 24 L20 16 L13 8 Z M18 8 L25 16 L18 24 L22 24 L29 16 L22 8 Z" fill="#fff"/></svg>
      <span class="benefit__text">Learn to shed pounds and rapidly reduce their waist size.</span>
    </li>
    <li class="benefit" style="top:50px">
      <svg class="benefit__icon" viewBox="0 0 36 32" aria-hidden="true"><rect width="36" height="32" rx="3" fill="var(--badge-blue)"/><path d="M9 8 L16 16 L9 24 L13 24 L20 16 L13 8 Z M18 8 L25 16 L18 24 L22 24 L29 16 L22 8 Z" fill="#fff"/></svg>
      <span class="benefit__text">Learn why weight loss doesn't work 99.9% of the time so that you can be the successful .1%.</span>
    </li>
    <li class="benefit" style="top:112px">
      <svg class="benefit__icon" viewBox="0 0 36 32" aria-hidden="true"><rect width="36" height="32" rx="3" fill="var(--badge-blue)"/><path d="M9 8 L16 16 L9 24 L13 24 L20 16 L13 8 Z M18 8 L25 16 L18 24 L22 24 L29 16 L22 8 Z" fill="#fff"/></svg>
      <span class="benefit__text">It's time to expose the LIES and reveal the TRUTH about the REAL causes of HEART DISEASE, DIABETES, CANCER, CHRONIC FATIGUE, ARTHRITIS, FIBROMYALGIA, and how to REVERSE /PREVENT this from ever happening to you or your family.</span>
    </li>
    <li class="benefit" style="top:220px">
      <svg class="benefit__icon" viewBox="0 0 36 32" aria-hidden="true"><rect width="36" height="32" rx="3" fill="var(--badge-blue)"/><path d="M9 8 L16 16 L9 24 L13 24 L20 16 L13 8 Z M18 8 L25 16 L18 24 L22 24 L29 16 L22 8 Z" fill="#fff"/></svg>
      <span class="benefit__text">The Insider Secrets to building your body into a health fortress unbreachable by sickness and disease.</span>
    </li>
    <li class="benefit" style="top:276px">
      <svg class="benefit__icon" viewBox="0 0 36 32" aria-hidden="true"><rect width="36" height="32" rx="3" fill="var(--badge-blue)"/><path d="M9 8 L16 16 L9 24 L13 24 L20 16 L13 8 Z M18 8 L25 16 L18 24 L22 24 L29 16 L22 8 Z" fill="#fff"/></svg>
      <span class="benefit__text">Learn to live and fufill your GOD-GIVEN health potential.</span>
    </li>
  </ul>

  <section class="gains">
    <h3 class="gains__title">It's not about what you lose&hellip; It's about what you gain&hellip;</h3>
    <ul class="gains__list">
      <li>The No-Hype, No-Gimmick secrets for fast effective Weight loss</li>
      <li>How heart disease, cancer and diabetes are linked to diet</li>
      <li>Tools and strategies to make 2012 the best year ever</li>
    </ul>
  </section>

  <div class="portrait-frame">
    <div class="portrait" role="img" aria-label="Portrait photo of the presenter in a dark suit and pink tie"></div>
  </div>
  <p class="speaker-name">Dr. Prent</p>

  <section class="venue">
    <h3 class="venue__title">Marlow Ridge College</h3>
    <div class="venue__map" role="img" aria-label="Street map showing the way to Marlow Ridge College"></div>
  </section>
</main>
</body>
</html>
```